Winter Soccer Training

Youth Soccer Academy, I want to advertise Winter Training $195.00(Includes training for one month, Uniform) after first Month $145 per month.

Target Market(s)

kids from 5 years to 18

Industry/Entity Type

Training

Colors
3176b5

Requirements
Must have
• Winter Training
• Location: Harbor Fieldhouse
• 4827 Maple Crest rd Larkwood MD 20993
• Phone:(240)555-0187
• Training Schedule
• Tuesday and Thursday
• 5:30pm to 6:30pm 5 to 10 years old
• 6:30pm to 7:30pm 11 to 15 years old
• 7:30pm to 8:30pm 16 to 19 years old
• www.velantoacademy.example
Nice to have
• Soccer Field
Should not have
• Soccer Balls

```html
<!DOCTYPE html>
<html lang="en">
<head>
<meta charset="utf-8">
<title>Velanto Soccer Academy – Winter Soccer Training</title>
<link href="https://fonts.googleapis.com/css2?family=Bebas+Neue&family=Arimo:wght@400&display=swap" rel="stylesheet">
<style>
  :root {
    --brand-blue: #3176b5;
    --tag-blue: #1f5ea8;
    --title-navy: #24307a;
    --ink: #161b26;
    --band-dark: #141618;
    --field-dark: #1c2620;
    --field-green: #33482f;
    --sky-top: #f4f8fb;
    --sky-mid: #c9dde2;
    --sky-low: #7e9aa0;
    --web-blue: #1e6fd2;
    --white: #ffffff;
    --silver-hi: #f2f4f5;
    --silver-lo: #8d9398;
  }
  * { margin: 0; padding: 0; box-sizing: border-box; }
  html, body { width: 927px; height: 1200px; overflow: hidden; background: #ffffff; }
  .flyer {
    position: relative;
    width: 927px;
    height: 1200px;
    overflow: hidden;
    font-family: "Bebas Neue", "Arial Narrow", sans-serif;
    color: var(--ink);
  }
  .backdrop-photo {
    position: absolute; left: 0; top: 0; width: 927px; height: 680px;
    background: linear-gradient(180deg, var(--sky-top) 0%, #e3eef2 22%, var(--sky-mid) 55%, var(--sky-low) 100%);
  }
  .field-photo {
    position: absolute; left: 0; top: 810px; width: 927px; height: 390px;
    background: radial-gradient(ellipse at 55% 55%, #4a4f4c 0%, var(--field-green) 45%, var(--field-dark) 100%);
  }
  .brand-mark {
    position: absolute; left: 73px; top: 60px; width: 272px;
    display: flex; flex-direction: column; align-items: center; gap: 18px;
  }
  .brand-mark .dot {
    width: 140px; height: 140px; border-radius: 50%; background: var(--brand-blue);
  }
  .brand-mark .name {
    font-size: 30px; letter-spacing: 1px; color: var(--title-navy); text-align: center; line-height: 1.05;
  }
  .academy-title {
    position: absolute; left: 383px; top: 50px;
    font-size: 64px; line-height: 58px; font-weight: 400; color: var(--title-navy);
  }
  .venue {
    position: absolute; left: 383px; top: 178px;
    font-size: 31px; line-height: 37px; letter-spacing: 0.5px; font-style: normal;
  }
  .schedule-tag {
    position: absolute; left: 381px; top: 314px; width: 276px; height: 40px;
  }
  .schedule-tag svg { position: absolute; inset: 0; }
  .schedule-tag span {
    position: relative; display: block; padding: 5px 0 0 11px;
    font-size: 32px; line-height: 34px; color: var(--white); letter-spacing: 0.5px;
  }
  .schedule {
    position: absolute; left: 383px; top: 366px;
    font-size: 31px; line-height: 34.5px; letter-spacing: 0.5px;
  }
  .director {
    position: absolute; left: 63px; top: 326px;
    font-size: 24px; line-height: 28px; letter-spacing: 0.5px;
  }
  .director .perks { margin-top: 18px; }
  .headline-winter {
    position: absolute; left: 0; top: 522px; width: 927px; text-align: center;
    font-size: 190px; line-height: 160px; letter-spacing: 6px; color: #f3f6f8;
    text-shadow: 0 2px 0 #b8c4cc, 0 4px 10px rgba(40,60,70,0.35);
  }
  .headline-winter span { display: inline-block; transform: scaleX(1.6); transform-origin: center; }
  .title-band {
    position: absolute; left: 0; top: 674px; width: 927px; height: 134px;
    background: linear-gradient(180deg, #2b2e31 0%, var(--band-dark) 20%, #0d0f10 80%, #2a2d30 100%);
    border-top: 3px solid #d9dde0; border-bottom: 3px solid #9aa1a6;
  }
  .headline-training {
    position: absolute; left: 0; top: 686px; width: 927px; text-align: center;
    font-size: 126px; line-height: 120px; font-weight: 400; letter-spacing: 8px; word-spacing: 30px;
    background: linear-gradient(180deg, var(--silver-hi) 0%, #c9cdd0 45%, var(--silver-lo) 55%, #dfe2e4 100%);
    -webkit-background-clip: text; background-clip: text; color: transparent;
  }
  .field-line {
    position: absolute; left: 0; top: 948px; width: 927px; height: 3px;
    background: linear-gradient(90deg, rgba(255,255,255,0.2), #e6e9eb 30%, #e6e9eb 70%, rgba(255,255,255,0.2));
  }
  .start-date {
    position: absolute; left: 39px; top: 984px;
    font-size: 37px; line-height: 40px; color: var(--white); letter-spacing: 1px;
  }
  .social-square {
    position: absolute; left: 34px; top: 1098px; width: 75px; height: 64px;
    background: #3a5a98; border-radius: 6px;
  }
  .website {
    position: absolute; left: 262px; top: 1140px;
    font-size: 30px; line-height: 34px; color: var(--web-blue); letter-spacing: 0.5px;
  }
  .price-seal {
    position: absolute; left: 590px; top: 908px; width: 300px; height: 290px;
  }
  .price-seal svg { position: absolute; inset: 0; }
  .price-seal .amount {
    position: absolute; left: 0; top: 66px; width: 292px; text-align: center;
    font-size: 88px; line-height: 88px; color: var(--white);
  }
  .price-seal .terms {
    position: absolute; left: 36px; top: 166px; width: 222px; text-align: center;
    font-family: "Arimo", Arial, sans-serif; font-size: 16px; line-height: 20px; color: var(--white);
  }
</style>
</head>
<body>
<main class="flyer">
  <div class="backdrop-photo" role="img" aria-label="Goalkeeper leaping in a snowy stadium under a pale winter sky"></div>
  <div class="field-photo" role="img" aria-label="Dark stadium pitch at night with a soccer ball on the grass"></div>

  <div class="brand-mark">
    <div class="dot"></div>
    <div class="name">Velanto Soccer Academy</div>
  </div>

  <h1 class="academy-title">Velanto<br>Soccer Academy</h1>

  <address class="venue">
    Harbor Fieldhouse<br>
    4827 Maple Crest Rd Larkwood MD 20993<br>
    Phone:(240)555-0187
  </address>

  <div class="schedule-tag">
    <svg width="276" height="40" viewBox="0 0 276 40"><polygon points="0,0 262,0 276,40 0,40" fill="var(--tag-blue)"/></svg>
    <span>Training Schedule</span>
  </div>

  <p class="schedule">
    Tuesday and Thursday<br>
    5:30pm to 6:30pm 5 to 10 years old<br>
    6:30pm to 7:30pm 11 to 15 years old<br>
    7:30pm to 8:30pm 16 to 19 years old
  </p>

  <div class="director">
    <p>Director: Marco Delvane<br>Ex Pro Soccer Player<br>Pro Coaching License A</p>
    <p class="perks">-Qualified Coaches<br>-Discipline and Training</p>
  </div>

  <div class="headline-winter"><span>Winter</span></div>
  <div class="title-band"></div>
  <h2 class="headline-training">Soccer Training</h2>
  <div class="field-line"></div>

  <p class="start-date">We Start<br>Nov 14,2017</p>

  <div class="social-square"></div>

  <p class="website">www.velantoacademy.example</p>

  <div class="price-seal">
    <svg width="300" height="290" viewBox="0 0 300 290">
      <defs>
        <radialGradient id="sealFill" cx="40%" cy="40%" r="70%">
          <stop offset="0%" stop-color="#1a78ec"/>
          <stop offset="100%" stop-color="#0a4fb0"/>
        </radialGradient>
        <linearGradient id="peelFill" x1="0" y1="0" x2="1" y2="1">
          <stop offset="0%" stop-color="#ffffff"/>
          <stop offset="100%" stop-color="#9aa2a8"/>
        </linearGradient>
      </defs>
      <circle cx="146" cy="144" r="142" fill="url(#sealFill)"/>
      <path d="M200 14 Q230 40 250 30 Q262 70 288 96 Q230 96 210 60 Q200 40 200 14 Z" fill="url(#peelFill)"/>
    </svg>
    <div class="amount">$195</div>
    <p class="terms">(INCLUDES FIRST MONTH AND UNIFORM) THE NEXT MONTHS $145.00.</p>
  </div>
</main>
</body>
</html>
```